Business card design needed

am looking for a fun and funky design to match our moto, seriously fun swimwear and fashion for girls.

We manufacture and retail girls swimwear and fashion in Australia. Our designs are fun loving and funky. I would like to use bright fuschia to match our website www.berrybloomwear.com.au. We target a higher end market so need it to reflect this.

Industry/Entity Type

Fashion

Contact Information for Business Card

Berry Bloom logo,
Melanie Drew
(07) 39514207
admin@berrybloomwear.com.au
www.berrybloomwear.com.au

Logo Text

Berry Bloom

```html
<!DOCTYPE html>
<html lang="en">
<head>
<meta charset="utf-8">
<title>Berry Bloom Business Card</title>
<link href="https://fonts.googleapis.com/css2?family=Oswald:wght@300;400;500&display=swap" rel="stylesheet">
<style>
  :root {
    --fuchsia-deep: #a80f57;
    --fuchsia: #c8186c;
    --fuchsia-bright: #d9287e;
    --blush-light: #f8f0f3;
    --blush: #e8d6de;
    --white: #ffffff;
    --rule: rgba(255,255,255,0.55);
    --page: #ece7e9;
  }
  * { box-sizing: border-box; margin: 0; padding: 0; }
  html, body { width: 1200px; height: 1024px; overflow: hidden; }
  body {
    background: var(--page);
    font-family: "Oswald", sans-serif;
    position: relative;
  }
  .card {
    position: absolute;
    left: 180px;
    width: 840px;
    height: 480px;
    overflow: hidden;
    box-shadow: 0 6px 18px rgba(0,0,0,0.15);
  }
  .card-front {
    top: 20px;
    background: radial-gradient(ellipse at 30% 40%, var(--fuchsia-bright), var(--fuchsia) 45%, var(--fuchsia-deep));
    color: var(--white);
  }
  .card-back {
    top: 524px;
    background: linear-gradient(160deg, var(--blush-light), var(--blush));
  }
  .divider-vertical {
    position: absolute;
    left: 430px; top: 0; bottom: 0;
    width: 1px;
    background: rgba(255,255,255,0.25);
  }
  .divider-horizontal {
    position: absolute;
    left: 430px; right: 0; top: 150px;
    height: 1px;
    background: var(--rule);
  }
  .brand {
    position: absolute;
    display: flex;
    align-items: center;
    gap: 16px;
  }
  .brand-mark {
    width: 46px; height: 46px;
    border-radius: 50%;
  }
  .brand-name {
    font-family: "Oswald", sans-serif;
    font-weight: 400;
    font-size: 46px;
    letter-spacing: 1px;
  }
  .card-front .brand { left: 60px; top: 300px; }
  .card-front .brand-mark { background: var(--white); }
  .card-front .brand-name { color: var(--white); }
  .contact-name {
    position: absolute;
    left: 470px; top: 166px;
    font-size: 40px;
    font-weight: 500;
    letter-spacing: 0.5px;
  }
  .contact-list {
    position: absolute;
    left: 470px; top: 236px;
    list-style: none;
  }
  .contact-list li {
    display: flex;
    align-items: center;
    gap: 14px;
    font-size: 22px;
    font-weight: 300;
    height: 42px;
  }
  .contact-list svg { width: 22px; height: 22px; flex: none; }
  .card-back .brand { left: 60px; top: 70px; }
  .card-back .brand-mark { background: var(--fuchsia); }
  .card-back .brand-name { color: var(--fuchsia); font-size: 52px; }
  .model-photo {
    position: absolute;
    right: 40px; bottom: 0;
    width: 330px; height: 300px;
    background: radial-gradient(ellipse at 50% 55%, #f3c6d8, #e9d8df 70%);
  }
</style>
</head>
<body>
  <section class="card card-front">
    <div class="divider-vertical"></div>
    <div class="divider-horizontal"></div>
    <div class="brand">
      <span class="brand-mark"></span>
      <span class="brand-name">Berry Bloom</span>
    </div>
    <h1 class="contact-name">Melanie Drew</h1>
    <ul class="contact-list">
      <li>
        <svg viewBox="0 0 24 24" aria-hidden="true"><path d="M6.6 10.8a15 15 0 0 0 6.6 6.6l2.2-2.2a1 1 0 0 1 1-.25 11.4 11.4 0 0 0 3.6.57 1 1 0 0 1 1 1V20a1 1 0 0 1-1 1A17 17 0 0 1 3 4a1 1 0 0 1 1-1h3.5a1 1 0 0 1 1 1c0 1.25.2 2.45.57 3.57a1 1 0 0 1-.25 1z" fill="#fff"/></svg>
        (07) 39514207
      </li>
      <li>
        <svg viewBox="0 0 24 24" aria-hidden="true"><circle cx="12" cy="12" r="11" fill="#fff"/><rect x="6" y="8" width="12" height="8" fill="none" stroke="#c8186c" stroke-width="1.5"/><path d="M6 8l6 5 6-5" fill="none" stroke="#c8186c" stroke-width="1.5"/></svg>
        admin@berrybloomwear.com.au
      </li>
      <li>
        <svg viewBox="0 0 24 24" aria-hidden="true"><circle cx="12" cy="12" r="11" fill="#fff"/><circle cx="12" cy="12" r="6.5" fill="none" stroke="#c8186c" stroke-width="1.3"/><path d="M5.5 12h13M12 5.5c-3 3.5-3 9.5 0 13M12 5.5c3 3.5 3 9.5 0 13" fill="none" stroke="#c8186c" stroke-width="1.3"/></svg>
        www.berrybloomwear.com.au
      </li>
    </ul>
  </section>

  <section class="card card-back">
    <div class="brand">
      <span class="brand-mark"></span>
      <span class="brand-name">Berry Bloom</span>
    </div>
    <div class="model-photo" role="img" aria-label="Photo of a girl posing in pink top and patterned leggings"></div>
  </section>
</body>
</html>
```